Business Card Design

Want something very unique. No business, just personal. The image I submitted is for inspiration only.

Target Market(s)

friends and new acquaintances

Industry/Entity Type

Business

Contact Information for Business Card

Mara Deltow
Santa Fe, NM
505-271-4906
maradeltow@quillbox.net

```html
<!DOCTYPE html>
<html lang="en">
<head>
<meta charset="utf-8">
<title>Mara Deltow – Personal Card</title>
<link rel="stylesheet" href="https://fonts.googleapis.com/css2?family=Audiowide&display=swap">
<style>
  :root {
    --backdrop: #e9e4dc;
    --card-dark: #3e2608;
    --card-mid: #573710;
    --accent: #f39a12;
    --accent-deep: #d9800a;
    --text-orange: #e58a12;
    --photo-light: #d8c2a6;
    --photo-mid: #a88466;
    --photo-dark: #6a4a30;
    --icon-red: #d92b2b;
    --white: #ffffff;
  }
  * { box-sizing: border-box; margin: 0; padding: 0; }
  html, body {
    width: 1174px;
    height: 1200px;
    overflow: hidden;
    background: var(--backdrop);
  }
  .canvas {
    position: relative;
    width: 1174px;
    height: 1200px;
  }
  .card {
    position: absolute;
    left: 37px;
    top: 294px;
    width: 1100px;
    height: 611px;
    background: radial-gradient(ellipse at 50% 38%, var(--card-mid) 0%, var(--card-dark) 75%);
    border-bottom: 9px solid var(--accent);
    box-shadow: 0 6px 18px rgba(0,0,0,0.25);
    font-family: "Audiowide", sans-serif;
    color: var(--text-orange);
  }
  .portrait {
    position: absolute;
    left: 383px;
    top: 58px;
    width: 334px;
    height: 334px;
    border-radius: 50%;
    background: var(--white);
    border: 9px solid var(--accent);
    padding: 9px;
    box-shadow: 0 4px 12px rgba(0,0,0,0.35);
  }
  .portrait-fill {
    width: 100%;
    height: 100%;
    border-radius: 50%;
    background: radial-gradient(circle at 45% 55%, var(--photo-light) 0%, var(--photo-mid) 55%, var(--photo-dark) 100%);
  }
  .name {
    position: absolute;
    left: 0;
    right: 0;
    top: 418px;
    text-align: center;
    font-size: 50px;
    letter-spacing: 3px;
    text-shadow: 0 2px 3px rgba(0,0,0,0.4);
  }
  .contact {
    position: absolute;
    left: 286px;
    display: flex;
    align-items: center;
    gap: 14px;
    font-size: 33px;
    letter-spacing: 1px;
  }
  .contact.phone { top: 499px; }
  .contact.email { top: 552px; font-size: 29px; }
  .contact svg { width: 32px; height: 32px; flex: none; }
</style>
</head>
<body>
<div class="canvas">
  <section class="card">
    <div class="portrait">
      <div class="portrait-fill" role="img" aria-label="Portrait photo of the card owner"></div>
    </div>
    <h1 class="name">Mara Deltow Santa Fe</h1>
    <p class="contact phone">
      <svg viewBox="0 0 32 32" aria-hidden="true">
        <rect x="1" y="1" width="30" height="30" rx="6" fill="var(--icon-red)"/>
        <path d="M10 7c1.5-1 3-.5 3.5 1l1 3c.3 1-.3 2-1.2 2.5l-.8.5c.8 2.5 2.8 4.5 5.3 5.3l.5-.8c.5-.9 1.5-1.5 2.5-1.2l3 1c1.5.5 2 2 1 3.5-1.5 2.5-4 3-7 1.5-4-2-7-5-9-9C7.5 11 8 8.5 10 7z" fill="var(--white)"/>
      </svg>
      <span>NM 505-271-4906</span>
    </p>
    <p class="contact email">
      <svg viewBox="0 0 32 32" aria-hidden="true">
        <rect x="2" y="6" width="28" height="20" rx="2" fill="var(--white)"/>
        <path d="M2 7l14 11L30 7" fill="none" stroke="var(--icon-red)" stroke-width="3"/>
      </svg>
      <span>maradeltow@quillbox.net</span>
    </p>
  </section>
</div>
</body>
</html>
```